Bramble Gate Stud

We have an existing website for our Thoroughbred Breeding and racing farm in The Plains Virginia we would like to improve it Our Web address is www.bramblegatestud.example
We also have a facebook page and a twitter account for our Stallion Moonlark whom we would like to Spotlight on our website. More Pictures and Info Available.
We would also like to work with the designer we choose to create our brochure for our farm. as well as some promotional material for our stallion Moonlark.
Please see the following competitor website, www.fenwaldacres.example we like the conservative and classic feel of this site design.
Updates

Project Deadline Extended
Reason: We want to give everyone a chance to make some changes we feel there have been some great ideas thus far. Thank you

Project Deadline Extended
Reason: Waiting on a few design changes from designers to come in.

Target Market(s)

Thoroughbred Breeders and Trainers

Industry/Entity Type

Conservative

Font styles to use
Sans Serif

Colors
3277b5
85abd2
0555a3
ffffff

Requirements
Must have
• Please see current website @ www.bramblegatestud.example

```html
<!DOCTYPE html>
<html lang="en">
<head>
<meta charset="utf-8">
<title>Bramble Gate Stud</title>
<link href="https://fonts.googleapis.com/css2?family=Questrial&family=Didact+Gothic&display=swap" rel="stylesheet">
<style>
  :root{
    --navy:#0a4a94;
    --navy-deep:#073d7c;
    --blue:#0555a3;
    --blue-mid:#3277b5;
    --blue-soft:#85abd2;
    --white:#ffffff;
    --yellow:#f7c800;
    --ink:#1b1b1b;
    --charcoal:#3d4549;
    --grey-box:#e9e9e9;
  }
  *{margin:0;padding:0;box-sizing:border-box}
  html,body{width:947px;height:1200px;overflow:hidden;background:var(--white)}
  body{position:relative;font-family:"Didact Gothic",sans-serif;color:var(--ink)}
  .head-font{font-family:"Questrial",sans-serif;text-transform:uppercase}

  /* Header */
  .site-header{position:absolute;left:0;top:0;width:947px;height:188px;
    background:radial-gradient(ellipse at 45% 60%,#4f5a5f 0%,#3d4549 55%,#2f3639 100%)}
  .brand{position:absolute;left:343px;top:34px;width:250px;display:flex;flex-direction:column;align-items:center}
  .brand-dot{width:34px;height:34px;border-radius:50%;background:var(--blue);flex:none}
  .brand-name{margin-top:16px;font-family:"Questrial",sans-serif;font-size:24px;line-height:29px;color:var(--white);text-transform:uppercase;letter-spacing:2px;text-align:center}
  .contact{position:absolute;left:712px;top:14px;display:flex;gap:8px;color:var(--white)}
  .contact-phone{font-family:"Questrial",sans-serif;font-size:17px;line-height:18px}
  .contact-address{font-family:"Questrial",sans-serif;font-size:8.5px;line-height:12px;text-transform:uppercase;letter-spacing:.3px}
  .social-bar{position:absolute;left:667px;top:75px;height:28px;display:flex}
  .social-lead{width:27px;height:28px;background:#2c3236;display:flex;align-items:center;justify-content:center}
  .social-list{width:166px;height:28px;background:var(--grey-box);display:flex;align-items:center;gap:7px;padding-left:15px}
  .social-item{width:17px;height:17px;background:#2c3236}

  /* Navigation */
  .main-nav{position:absolute;left:0;top:188px;width:947px;height:44px;background:var(--navy)}
  .nav-list{list-style:none;display:flex;position:absolute;left:93px;top:0;height:44px}
  .nav-item{font-family:"Questrial",sans-serif;font-size:11.5px;color:var(--white);text-transform:uppercase;padding:0 11px;line-height:44px}
  .nav-item.is-active{background:var(--blue);border-top:3px solid var(--yellow);line-height:38px}
  .nav-search{position:absolute;left:834px;top:10px;width:24px;height:24px;border-radius:50%;background:var(--blue-mid);display:flex;align-items:center;justify-content:center}

  /* Hero */
  .hero{position:absolute;left:0;top:232px;width:947px;height:384px;
    background:linear-gradient(90deg,#8a8a4e 0%,#9b6a36 25%,#a65a28 50%,#8d7a47 75%,#7d8e4f 100%)}
  .hero-arrow{position:absolute;top:179px;width:32px;height:32px;border-radius:50%;background:rgba(60,60,60,.55);display:flex;align-items:center;justify-content:center}
  .hero-arrow.prev{left:88px}
  .hero-arrow.next{left:830px}
  .feature-panel{position:absolute;left:144px;top:232px;width:283px;height:107px;background:var(--blue);padding:13px 15px 0 17px;color:var(--white)}
  .feature-title{font-family:"Questrial",sans-serif;font-size:14px;color:var(--yellow);text-transform:uppercase;padding-bottom:6px;border-bottom:1px solid rgba(255,255,255,.35)}
  .feature-text{font-size:9.5px;line-height:13px;margin-top:6px;text-align:justify}
  .feature-more{display:block;text-align:right;font-family:"Questrial",sans-serif;font-size:8.5px;text-transform:uppercase;text-decoration:underline;margin-top:3px;color:var(--white)}

  /* Tagline band */
  .tagline-band{position:absolute;left:0;top:616px;width:947px;height:104px;background:var(--navy)}
  .tagline{position:absolute;left:0;width:947px;top:16px;text-align:center;font-size:22px;color:var(--white);letter-spacing:.5px}
  .tagline-bar{position:absolute;left:417px;top:45px;width:113px;height:4px;background:var(--blue-soft)}
  .tagline-rule{position:absolute;left:88px;top:50px;width:771px;height:1px;background:rgba(255,255,255,.15)}
  .brochure-btn{position:absolute;left:365px;top:62px;width:196px;height:34px;background:var(--yellow);color:var(--ink);font-size:14px;display:flex;align-items:center;justify-content:center;box-shadow:0 2px 3px rgba(0,0,0,.3)}

  /* Features */
  .features{position:absolute;left:0;top:720px;width:947px;height:380px;
    background:linear-gradient(180deg,#b8d3ee 0%,#dbe8f5 30%,#ffffff 60%,#ffffff 100%)}
  .feature-card{position:absolute;top:37px;width:198px;text-align:center}
  .feature-card:nth-child(1){left:88px}
  .feature-card:nth-child(2){left:375px}
  .feature-card:nth-child(3){left:663px}
  .card-photo{width:198px;height:134px;border:5px solid var(--white);box-shadow:2px 3px 5px rgba(0,0,0,.3)}
  .card-title{font-size:12.5px;color:var(--ink);margin-top:28px;padding-bottom:7px;border-bottom:1px solid #d5d5d5;position:relative}
  .card-title::after{content:"";position:absolute;left:62px;bottom:-3px;width:74px;height:4px;background:var(--blue)}
  .card-text{font-size:10.5px;line-height:14.5px;margin-top:9px;padding:0 2px}
  .card-btn{display:inline-flex;width:93px;height:32px;margin-top:21px;background:var(--blue);color:var(--white);font-size:11px;align-items:center;justify-content:center}

  /* Footer */
  .site-footer{position:absolute;left:0;top:1100px;width:947px;height:100px;
    background:linear-gradient(180deg,#6a9e2a 0%,#4c7d1c 28%,#3a2a1a 55%,#231810 100%)}
  .footer-copy{position:absolute;top:75px;left:87px;font-size:9.5px;color:var(--white)}
</style>
</head>
<body>

<header class="site-header" role="img" aria-label="Photo of a rider in a tweed riding jacket behind the farm name">
  <div class="brand">
    <span class="brand-dot"></span>
    <span class="brand-name">Bramble Gate<br>Stud</span>
  </div>
  <div class="contact">
    <svg width="22" height="30" viewBox="0 0 22 30" aria-hidden="true">
      <path d="M5 2 L10 2 L11 9 L7 11 Q9 18 14 22 L17 19 L21 22 L19 28 Q8 27 3 14 Q1 6 5 2 Z" fill="none" stroke="#85abd2" stroke-width="2" stroke-linejoin="round"/>
    </svg>
    <div>
      <div class="contact-phone">(540) 555-0148</div>
      <div class="contact-address">412 Bramble Gate Road<br>Ashcombe, VA 20100</div>
    </div>
  </div>
  <div class="social-bar">
    <div class="social-lead">
      <svg width="11" height="11" viewBox="0 0 11 11" aria-hidden="true"><circle cx="5.5" cy="3" r="2.5" fill="#fff"/><path d="M1 11 Q1 6 5.5 6 Q10 6 10 11 Z" fill="#fff"/></svg>
    </div>
    <div class="social-list">
      <span class="social-item"></span><span class="social-item"></span><span class="social-item"></span>
      <span class="social-item"></span><span class="social-item"></span><span class="social-item"></span>
    </div>
  </div>
</header>

<nav class="main-nav">
  <ul class="nav-list">
    <li class="nav-item">Home</li>
    <li class="nav-item is-active">Stallions</li>
    <li class="nav-item">Mares and Foals</li>
    <li class="nav-item">Horses in Training</li>
    <li class="nav-item">About Our Facility</li>
    <li class="nav-item">Contact</li>
  </ul>
  <div class="nav-search">
    <svg width="10" height="10" viewBox="0 0 10 10" aria-hidden="true"><circle cx="4" cy="4" r="3" fill="none" stroke="#fff" stroke-width="1.5"/><line x1="6.2" y1="6.2" x2="9" y2="9" stroke="#fff" stroke-width="1.5"/></svg>
  </div>
</nav>

<section class="hero" role="img" aria-label="Photo of a chestnut horse with a white blaze under a rider in a dressage arena">
  <div class="hero-arrow prev"><svg width="10" height="12" viewBox="0 0 10 12" aria-hidden="true"><polyline points="7,1 2,6 7,11" fill="none" stroke="#ddd" stroke-width="2"/></svg></div>
  <div class="hero-arrow next"><svg width="10" height="12" viewBox="0 0 10 12" aria-hidden="true"><polyline points="3,1 8,6 3,11" fill="none" stroke="#ddd" stroke-width="2"/></svg></div>
</section>

<aside class="feature-panel">
  <h2 class="feature-title">Moonlark</h2>
  <p class="feature-text">A winner of seven races and $816,277, Northvale-bred Stallion Moonlark (GB), By Allegro Sky and out of Quiet Harbour, retired sound after racing in top company at distances from 5-1/2 furlongs to one mile.</p>
  <span class="feature-more">Read More</span>
</aside>

<section class="tagline-band">
  <h1 class="tagline head-font">Thoroughbred Breeding and Racing at it's Best!</h1>
  <div class="tagline-rule"></div>
  <div class="tagline-bar"></div>
  <div class="brochure-btn head-font">Download Brochure</div>
</section>

<section class="features">
  <article class="feature-card">
    <div class="card-photo" role="img" aria-label="Photo of a bay stallion standing in front of a white house" style="background:linear-gradient(180deg,#d8d6cc 0%,#6b4a32 50%,#7b8b5a 100%)"></div>
    <h3 class="card-title head-font">Stallions</h3>
    <p class="card-text">Lorem Ipsum Is simply dummy text. Lorem Ipsum Is simply dummy text. Lorem Ipsum Is simply dummy text. Lorem Ipsum Is simply dummy text.</p>
    <span class="card-btn head-font">Read More</span>
  </article>
  <article class="feature-card">
    <div class="card-photo" role="img" aria-label="Photo of the farm entrance sign beside a fenced lane" style="background:linear-gradient(180deg,#c9c7b0 0%,#8e9a52 45%,#6e7e3c 100%)"></div>
    <h3 class="card-title head-font">Bramble Gate Stud</h3>
    <p class="card-text">Lorem Ipsum Is simply dummy text. Lorem Ipsum Is simply dummy text. Lorem Ipsum Is simply dummy text. Lorem Ipsum Is simply dummy text.</p>
    <span class="card-btn head-font">Read More</span>
  </article>
  <article class="feature-card">
    <div class="card-photo" role="img" aria-label="Photo of racehorses and jockeys at full gallop" style="background:linear-gradient(135deg,#3a3a3a 0%,#6a4028 50%,#8a5a3a 100%)"></div>
    <h3 class="card-title head-font">Horse Riding</h3>
    <p class="card-text">Lorem Ipsum Is simply dummy text. Lorem Ipsum Is simply dummy text. Lorem Ipsum Is simply dummy text. Lorem Ipsum Is simply dummy text.</p>
    <span class="card-btn head-font">Read More</span>
  </article>
</section>

<footer class="site-footer" role="img" aria-label="Grass and soil strip">
  <span class="footer-copy">Copyright © 2014 All Right Reserved</span>
</footer>

</body>
</html>
```